out of the box Business Card Design for a Manufacturer / Distributor

We are a manufarturer and distributor of products.
the company name is VORTANI (Pic attached)

the picture is NOT a must have on the business Card.

the Business Card should look really professional and/or special, so out of the box thinking is welcome.

there should be 2 Adresses on the Business Card for Main and Branch Office.
Email Adress, homepage, Name is required
NO Phone Number

Our working field:
Private Labeling
high Quality Production
direct distribution
warehousing
trademark registration
legal support

Main Office:
Kornblumenweg 14
08352 Eschenfeld
Austria

Branch Office:
Daska Lane
Karvelle
Malaysia

Names:
Lukas Feldhaus (Owner)
Imran Qureshi (Owner)

Email:
lukas@vortani-example.com
imran@vortani-example.com

homepage:
vortani-example.com

Industry/Entity Type

Manufacturer Distributer

Contact Information for Business Card

Vortani

Requirements
Must have
• Names, both office Adresses, email, homepage
Should not have
• Phone Number

```html
<!DOCTYPE html>
<html lang="en">
<head>
<meta charset="utf-8">
<title>Vortani — Business Card</title>
<link rel="stylesheet" href="https://fonts.googleapis.com/css2?family=Open+Sans:wght@400&family=Roboto+Condensed:wght@400;700&display=swap">
<style>
  :root {
    --orange: #f2722c;
    --ink: #231f20;
    --paper: #ffffff;
    --shadow: rgba(0, 0, 0, 0.85);
  }
  html, body {
    margin: 0;
    padding: 0;
    width: 1200px;
    height: 1200px;
    overflow: hidden;
    background: var(--paper);
  }
  .canvas {
    position: relative;
    width: 1200px;
    height: 1200px;
  }
  .card {
    position: absolute;
    width: 709px;
    height: 405px;
    background: var(--orange);
    box-shadow: 16px 14px 12px var(--shadow);
    overflow: hidden;
  }
  .card--front { left: 249px; top: 84px; }
  .card--back  { left: 247px; top: 654px; width: 710px; }
  .card__art {
    position: absolute;
    inset: 0;
    width: 100%;
    height: 100%;
  }
  .hex { filter: drop-shadow(0 0 14px rgba(0, 0, 0, 0.55)); }

  .brand {
    position: absolute;
    display: flex;
    align-items: center;
    font-family: "Open Sans", sans-serif;
    font-weight: 400;
    line-height: 1;
  }
  .brand__dot { border-radius: 50%; flex: none; }
  .brand--front { left: 99px; top: 173px; gap: 22px; color: var(--paper); }
  .brand--front .brand__dot { width: 54px; height: 54px; background: var(--paper); }
  .brand--front .brand__name { font-size: 54px; letter-spacing: 1px; }
  .brand--back { left: 14px; top: 30px; gap: 14px; color: var(--orange); }
  .brand--back .brand__dot { width: 38px; height: 38px; background: var(--orange); }
  .brand--back .brand__name { font-size: 37px; letter-spacing: 0.5px; }

  .website {
    position: absolute;
    right: 88px;
    top: 377px;
    font-family: "Open Sans", sans-serif;
    font-size: 16px;
    letter-spacing: 2.2px;
    color: var(--paper);
    line-height: 1;
  }

  .owners {
    position: absolute;
    left: 310px;
    width: 314px;
    top: 41px;
    height: 329px;
    display: flex;
    flex-direction: column;
    align-items: center;
    justify-content: center;
    gap: 8px;
    font-family: "Roboto Condensed", sans-serif;
    font-weight: 700;
    color: var(--orange);
    text-transform: uppercase;
    line-height: 1.05;
  }
  .owners__name { font-size: 38px; letter-spacing: -0.6px; white-space: nowrap; }
  .owners__join { font-size: 36px; }

  .contact {
    position: absolute;
    left: 6px;
    display: flex;
    align-items: center;
    gap: 12px;
    font-family: "Roboto Condensed", sans-serif;
    font-weight: 400;
    font-size: 13px;
    line-height: 17px;
    color: var(--paper);
  }
  .contact--address { top: 302px; }
  .contact--email { top: 351px; }
  .contact__icon { width: 32px; flex: none; display: flex; justify-content: center; }
  .contact__lines p { margin: 0; white-space: nowrap; }
</style>
</head>
<body>
<main class="canvas">

  <section class="card card--front" aria-label="Business card front">
    <svg class="card__art" viewBox="0 0 709 405" aria-hidden="true">
      <polygon points="284,0 709,0 709,405 284,405 168,202" fill="var(--ink)"/>
      <polygon class="hex" points="147.5,35 337.5,35 432,199 337.5,363 147.5,363 53,199" fill="var(--ink)"/>
    </svg>
    <div class="brand brand--front">
      <span class="brand__dot"></span>
      <span class="brand__name">VORTANI</span>
    </div>
    <div class="website">WWW.VORTANI-EXAMPLE.COM</div>
  </section>

  <section class="card card--back" aria-label="Business card back">
    <svg class="card__art" viewBox="0 0 710 405" aria-hidden="true">
      <polygon points="0,0 426,0 543,202 426,405 0,405" fill="var(--ink)"/>
      <polygon class="hex" points="371,41 563,41 657,206 563,370 371,370 277.5,206" fill="var(--ink)"/>
    </svg>
    <div class="brand brand--back">
      <span class="brand__dot"></span>
      <span class="brand__name">VORTANI</span>
    </div>

    <div class="owners">
      <span class="owners__name">Lukas Feldhaus</span>
      <span class="owners__join">&amp;</span>
      <span class="owners__name">Imran Qureshi</span>
    </div>

    <div class="contact contact--address">
      <span class="contact__icon">
        <svg width="25" height="31" viewBox="0 0 25 31" aria-hidden="true">
          <path d="M12.5 30.5 C5 20.5 1 15 1 11.5 A11.5 11.5 0 0 1 24 11.5 C24 15 20 20.5 12.5 30.5 Z" fill="var(--orange)"/>
          <circle cx="12.5" cy="11.5" r="4.5" fill="var(--ink)"/>
        </svg>
      </span>
      <div class="contact__lines">
        <p>(MAIN OFF)Kornblumenweg 14, 08352 Eschenfeld, Austria</p>
        <p>(BRANCH OFF)Daska Lane, Karvelle, Malaysia</p>
      </div>
    </div>

    <div class="contact contact--email">
      <span class="contact__icon">
        <svg width="30" height="21" viewBox="0 0 30 21" aria-hidden="true">
          <rect x="1.5" y="1.5" width="27" height="18" rx="2.5" fill="none" stroke="var(--orange)" stroke-width="2.5"/>
          <path d="M2.5 3 L15 12.5 L27.5 3" fill="none" stroke="var(--orange)" stroke-width="2.5" stroke-linejoin="round"/>
        </svg>
      </span>
      <div class="contact__lines">
        <p>lukas@vortani-example.com</p>
        <p>imran@vortani-example.com</p>
      </div>
    </div>
  </section>

</main>
</body>
</html>
```